Yard Sign Design Needed

Yard sign needed for mowing & landscaping company. Would like to use the top logo with black background which is attached. Would like MOWING to be in large standout letters. The word "landscaping" can be smaller and more artistic or omitted. Will need room for phone number once design is approved. The phone number will need to stand out and look identical/similar to the word 'MOWING"

```html
<!DOCTYPE html>
<html lang="en">
<head>
<meta charset="utf-8">
<title>Bramlow Contractors – Mowing Yard Sign</title>
<link href="https://fonts.googleapis.com/css2?family=Michroma&family=Montserrat:wght@700;800;900&family=Oswald:wght@500&display=swap" rel="stylesheet">
<style>
  :root {
    --green: #8cab0e;
    --black: #000000;
    --white: #ffffff;
    --page: #ffffff;
    --shadow: rgba(0, 0, 0, 0.18);
  }
  html, body {
    margin: 0;
    padding: 0;
    width: 1200px;
    height: 658px;
    overflow: hidden;
    background: var(--page);
  }
  .canvas {
    position: relative;
    width: 1200px;
    height: 658px;
  }
  .yard-sign {
    position: absolute;
    left: 403px;
    top: 51px;
    width: 393px;
    height: 556px;
    background: var(--white);
    box-shadow: 1px 2px 5px var(--shadow);
    overflow: hidden;
  }
  .header-shape {
    position: absolute;
    left: 0;
    top: 0;
    width: 393px;
    height: 556px;
  }
  .inner-frame {
    position: absolute;
    left: 16px;
    top: 13px;
    width: 357px;
    height: 526px;
    border: 2px solid var(--green);
  }
  .brand-mark {
    position: absolute;
    left: 156px;
    top: 74px;
    width: 80px;
    height: 80px;
    border-radius: 50%;
    background: var(--green);
  }
  .brand-name {
    position: absolute;
    left: 0;
    width: 393px;
    margin: 0;
    text-align: center;
    font-family: "Michroma", sans-serif;
    font-weight: 400;
    line-height: 1;
    white-space: nowrap;
  }
  .brand-name--main {
    top: 210px;
    font-size: 36px;
    letter-spacing: 0;
    color: var(--green);
  }
  .brand-name--sub {
    top: 255px;
    font-size: 20px;
    letter-spacing: 0.5px;
    color: var(--white);
  }
  .brand-suffix {
    position: absolute;
    left: 75px;
    top: 283px;
    width: 244px;
    display: flex;
    align-items: center;
    gap: 10px;
    font-family: "Michroma", sans-serif;
    font-size: 12px;
    line-height: 1;
    color: var(--white);
  }
  .brand-suffix::before,
  .brand-suffix::after {
    content: "";
    flex: 1;
    height: 1px;
    background: var(--white);
  }
  .service-title {
    position: absolute;
    left: 0;
    top: 346px;
    width: 393px;
    margin: 0;
    text-align: center;
    font-family: "Montserrat", sans-serif;
    font-weight: 900;
    font-size: 70px;
    letter-spacing: -2.5px;
    line-height: 1;
    color: var(--black);
  }
  .grass-strip {
    position: absolute;
    left: 16px;
    top: 438px;
    width: 361px;
    height: 22px;
    background: linear-gradient(to bottom, rgba(140, 171, 14, 0.2), var(--green));
  }
  .service-subtitle {
    position: absolute;
    left: 0;
    top: 419px;
    width: 393px;
    margin: 0;
    text-align: center;
    font-family: "Oswald", sans-serif;
    font-weight: 500;
    font-size: 40px;
    line-height: 1;
    letter-spacing: -0.5px;
    color: var(--green);
  }
  .contact-panel {
    position: absolute;
    left: 16px;
    top: 458px;
    width: 361px;
    height: 85px;
    background: var(--green);
    overflow: hidden;
  }
  .phone-icon {
    position: absolute;
    left: 6px;
    top: 16px;
    width: 52px;
    height: 56px;
  }
  .phone-number {
    position: absolute;
    left: 66px;
    top: 10px;
    margin: 0;
    font-family: "Montserrat", sans-serif;
    font-weight: 800;
    font-size: 38px;
    line-height: 1;
    letter-spacing: 0.3px;
    color: var(--white);
    white-space: nowrap;
  }
  .website {
    position: absolute;
    left: 72px;
    top: 51px;
    margin: 0;
    font-family: "Montserrat", sans-serif;
    font-weight: 700;
    font-size: 17px;
    line-height: 1;
    letter-spacing: 1.4px;
    color: var(--white);
    white-space: nowrap;
  }
</style>
</head>
<body>
<main class="canvas">
  <article class="yard-sign">
    <svg class="header-shape" viewBox="0 0 393 556" aria-hidden="true">
      <path d="M0 0 H393 V284 Q196.5 358 0 284 Z" fill="var(--black)"/>
      <path d="M0 289 Q196.5 363 393 289" fill="none" stroke="var(--green)" stroke-width="9"/>
    </svg>

    <div class="inner-frame"></div>

    <div class="brand-mark"></div>
    <p class="brand-name brand-name--main">BRAMLOW</p>
    <p class="brand-name brand-name--sub">CONTRACTORS</p>
    <p class="brand-suffix">LLC</p>

    <h1 class="service-title">MOWING</h1>

    <div class="grass-strip" role="img" aria-label="Grass blade border"></div>
    <h2 class="service-subtitle">LANDSCAPING</h2>

    <section class="contact-panel">
      <svg class="phone-icon" viewBox="0 0 52 56" aria-hidden="true">
        <path d="M4 30 Q4 22 14 20 L18 20 L18 50 L12 50 Q4 48 4 40 Z" fill="var(--white)"/>
        <rect x="16" y="2" width="26" height="50" rx="4" fill="var(--white)"/>
        <rect x="20" y="8" width="18" height="36" fill="var(--green)"/>
        <circle cx="29" cy="48" r="1.8" fill="var(--green)"/>
        <rect x="38" y="18" width="10" height="6" rx="3" fill="var(--white)"/>
        <rect x="38" y="26" width="10" height="6" rx="3" fill="var(--white)"/>
        <rect x="38" y="34" width="10" height="6" rx="3" fill="var(--white)"/>
        <path d="M24 22 a8 8 0 0 1 8 8 M24 26 a4 4 0 0 1 4 4" fill="none" stroke="var(--white)" stroke-width="1.8"/>
      </svg>
      <p class="phone-number">0198 765 432</p>
      <p class="website">www.bramlowlawns.com</p>
    </section>
  </article>
</main>
</body>
</html>
```